Bref créative |
Personal Chef Website Design | ||
New Website | ||
Chef / Catering | ||
www.lenasharvesttable.com | ||
Lena's Harvest Table prepares fresh, ready-to-cook gourmet dinners for on-the-go families with twice a week home delivery. All dinners are prepared weekly with fresh ingredients using the same care and passion Lena uses to prepare dinners for her own family. | ||
See creative brief uploaded as separate doc. Typically like bright, vibrant colors. The most influential colors in terms of food are: red, orange, yellow. An easy to read and use site is important to us |
Clean/Simple Friendly Family Oriented Colorful Service Oriented Feminine |
top | ||
www.fitplatehub.com | ||
www.suppernest.com | ||
facebook.com/lenasharvesttable | ||
See separate creative brief doc, logo and images for use in designing the site. If you have any questions or need further clarity on anything, don't hesitate to ask. | ||

```html
<!DOCTYPE html>
<html lang="en">
<head>
<meta charset="utf-8">
<title>Lena's Harvest Table</title>
<link href="https://fonts.googleapis.com/css2?family=Open+Sans:wght@400;600;700&display=swap" rel="stylesheet">
<style>
:root{
  --green:#6b9b1e;
  --green-dark:#4f7a10;
  --red:#c7281c;
  --orange:#e68a1c;
  --blue:#2f7fc1;
  --beige:#efe8d3;
  --beige-stripe:#e8dfc5;
  --footer:#e3d8b9;
  --ink:#4a4a4a;
  --muted:#8a8a8a;
  --line:#ddd6c4;
  --white:#ffffff;
}
*{box-sizing:border-box;margin:0;padding:0}
html,body{width:1200px;height:1062px;overflow:hidden}
body{font-family:"Open Sans",sans-serif;color:var(--ink);font-size:10px;
  background:repeating-linear-gradient(90deg,var(--beige) 0 22px,var(--beige-stripe) 22px 44px);position:relative}
.page{position:absolute;left:222px;top:0;width:756px;height:872px;background:var(--white);box-shadow:0 0 8px rgba(0,0,0,.12);overflow:hidden}
.util{position:absolute;right:0;top:0;background:var(--red);color:#fff;font-size:9px;padding:2px 10px;height:15px}
.util span{margin:0 4px}
.nav{position:absolute;top:18px;left:0;width:100%;height:52px;z-index:2}
.nav a{position:absolute;color:var(--green);font-weight:600;font-size:14px;text-decoration:none;line-height:16px;text-align:center}
.brand{position:absolute;left:288px;top:-6px;width:180px;text-align:center}
.brand .mark{width:38px;height:38px;border-radius:50%;background:var(--green);margin:0 auto 2px}
.brand b{display:block;color:var(--green-dark);font-size:12px;font-weight:700;white-space:nowrap;line-height:14px}
.hero{position:absolute;left:8px;top:72px;width:740px;height:224px;
  background:radial-gradient(circle at 30% 60%,#f3c34a,transparent 40%),radial-gradient(circle at 75% 40%,#e35a2a,transparent 45%),linear-gradient(120deg,#b8321c,#e88a2e 50%,#c23b20)}
.hero .cap{position:absolute;left:0;bottom:30px;width:360px;background:rgba(60,30,10,.7);color:#fff;padding:8px 14px}
.hero .cap h2{font-size:18px;font-weight:700;color:#ffd35a}
.hero .cap p{font-size:9px;line-height:12px}
.arrow{position:absolute;top:100px;width:26px;height:26px;border-radius:50%;background:rgba(255,255,255,.85)}
.dots{position:absolute;right:16px;bottom:10px;display:flex;gap:5px}
.dots i{width:9px;height:9px;border-radius:50%;background:rgba(255,255,255,.6)}
.dots i:first-child{background:#fff}
.promos{position:absolute;left:8px;top:304px;width:740px;display:flex;gap:10px}
.promo{flex:1;height:108px;border:1px solid var(--line);padding:8px;position:relative}
.promo small{display:block;font-size:8px;color:var(--muted)}
.promo .big{font-size:32px;font-weight:700;line-height:36px}
.promo p{font-size:8px;width:120px;line-height:11px}
.promo .pic{position:absolute;right:8px;top:14px;width:92px;height:78px;border-radius:6px}
.g{color:var(--green)}.r{color:var(--red)}.o{color:var(--orange)}
.left{position:absolute;left:8px;top:424px;width:486px}
.right{position:absolute;left:506px;top:424px;width:242px}
.head{display:flex;justify-content:space-between;align-items:flex-end;border-bottom:1px solid var(--line);padding-bottom:3px;margin-bottom:7px}
.head h3{font-size:14px;color:var(--green-dark);font-weight:700;line-height:18px}
.head a{font-size:9px;color:var(--muted);text-decoration:none}
.how{display:flex;gap:12px;height:104px;margin-bottom:10px}
.how .pic{width:150px;height:104px;background:linear-gradient(135deg,#8aa04a,#d9a544,#b2482a);flex:none}
.how p{font-size:9px;line-height:12px;margin-bottom:3px}
.menu{display:flex;gap:10px;margin-bottom:10px}
.card{flex:1;border:1px solid var(--line)}
.card h4{color:#fff;font-size:10px;padding:4px 8px}
.card .pic{height:50px;background:linear-gradient(120deg,#d8532a,#f2b441,#9a3a1e)}
.card .body{display:flex;justify-content:space-between;align-items:center;padding:5px 8px}
.card ul{list-style:none;font-size:8.5px;line-height:12px}
.card ul li::before{content:"• ";color:var(--green)}
.card .badge{width:34px;height:34px;border-radius:50%}
.duo{display:flex;gap:14px}
.duo>div{flex:1}
.duo p{font-size:8.5px;line-height:11px}
.duo .q{font-style:italic;color:var(--muted)}
.box{border:1px solid var(--line);margin-bottom:8px}
.box h3{color:#fff;font-size:12px;padding:4px 8px;font-weight:700}
.search{padding:2px 0 6px}
.search h3{color:var(--green-dark);font-size:13px;margin-bottom:4px}
.row{display:flex;gap:6px;align-items:center}
.field{border:1px solid #cfc8b6;height:18px;background:#fff;flex:1}
.btn{color:#fff;font-size:9px;font-weight:600;padding:3px 12px}
.calc{padding:7px 8px;font-size:9px}
.calc .row{margin-bottom:6px}
.calc .small{flex:none;width:44px}
.radio{width:9px;height:9px;border:1px solid #999;border-radius:50%;display:inline-block;vertical-align:middle}
.touch{padding:6px 8px;font-size:9px}
.touch label{display:block;color:var(--muted);margin-bottom:2px;line-height:11px}
.touch .field{display:block;margin-bottom:6px;height:16px}
.touch .area{height:42px}
.footer{position:absolute;left:0;top:872px;width:1200px;height:140px;background:var(--footer)}
.fcols{position:absolute;left:230px;top:12px;width:740px;display:flex;gap:30px}
.fcols>div{flex:1}
.fcols h4{font-size:12px;color:var(--green-dark);border-bottom:1px solid #c9bd99;padding-bottom:3px;margin-bottom:6px}
.fcols ul{list-style:none;font-size:9px;line-height:15px}
.fcols .soc li{display:flex;align-items:center;gap:6px;margin-bottom:4px;font-weight:600}
.fcols .soc i{width:14px;height:14px;display:inline-block}
.bottom{position:absolute;left:0;top:1012px;width:1200px;height:50px;background:var(--white)}
.bottom .logo{position:absolute;left:232px;top:14px;display:flex;align-items:center;gap:6px;color:var(--green-dark);font-weight:700;font-size:14px}
.bottom .logo i{width:18px;height:18px;border-radius:50%;background:var(--green)}
.bottom .copy{position:absolute;right:232px;top:18px;font-size:9px;color:var(--muted)}
</style>
</head>
<body>
<div class="page">
  <div class="util"><span>Other Site</span>|<span>My Account</span>|<span>Shop Online</span></div>
  <nav class="nav">
    <a style="left:30px;top:18px">Home</a>
    <a style="left:90px;top:18px">How it Works</a>
    <a style="left:196px;top:18px">The Kitchen</a>
    <div class="brand"><div class="mark"></div><b>Lena's Harvest Table</b></div>
    <a style="left:470px;top:10px">Our Current<br>Menu</a>
    <a style="left:565px;top:10px">Catering<br>Services</a>
    <a style="left:650px;top:10px">Lena's<br>Passion</a>
  </nav>

  <div class="hero" role="img" aria-label="Photo of a fresh homemade pizza and dishes">
    <div class="arrow" style="left:10px"></div>
    <div class="arrow" style="right:10px"></div>
    <div class="cap"><h2>From My Kitchen To Yours</h2><p>Fresh, ready-to-cook gourmet dinners delivered to your door twice a week.<br>Prepared with the same care I give my own family.</p></div>
    <div class="dots"><i></i><i></i><i></i><i></i></div>
  </div>

  <div class="promos">
    <div class="promo"><small class="g">Get Your Dinner</small><div class="big g">Free</div><p>Invite a friend and your next dinner is on us. <b class="g">Learn more</b></p><div class="pic" role="img" aria-label="Plated dinner photo" style="background:linear-gradient(135deg,#9bb54a,#e0b24a)"></div></div>
    <div class="promo"><small class="o">Delivery fee</small><div class="big o">$0.00</div><p>No delivery charge on all weekly plans. <b class="o">Learn more</b></p><div class="pic" role="img" aria-label="Delivery meal photo" style="background:linear-gradient(135deg,#e7a23a,#c9552a)"></div></div>
    <div class="promo"><small class="r">Delivery is</small><div class="big r">Free</div><p>Twice a week, straight to your home. <b class="r">Learn more</b></p><div class="pic" role="img" aria-label="Fresh salad photo" style="background:linear-gradient(135deg,#d2452a,#86a63a)"></div></div>
  </div>

  <div class="left">
    <div class="head"><h3>How it works</h3><a>» view all</a></div>
    <div class="how">
      <div class="pic" role="img" aria-label="Photo of a prepared gourmet dinner"></div>
      <div>
        <p>Lena's Harvest Table prepares fresh, ready-to-cook gourmet dinners for on-the-go families with twice a week home delivery. All dinners are prepared weekly with fresh ingredients using the same care and passion Lena uses for her own family.</p>
        <p><b class="g">Getting started is easy:</b></p>
        <p>1) Log on to www.lenasharvesttable.com 2) Look through our current dinner menu 3) Choose your plan and delivery day. Then simply cook, serve and enjoy your evening together.</p>
      </div>
    </div>
    <div class="head"><h3>Our current menu</h3><a>» view all</a></div>
    <div class="menu">
      <div class="card"><h4 style="background:var(--green)">Basic 4 - Weeks</h4><div class="pic" role="img" aria-label="Pizza photo"></div><div class="body"><ul><li>Advantage no.1</li><li>Advantage no.2</li><li>Advantage no.3</li><li>Advantage no.4</li></ul><i class="badge" style="background:var(--green)"></i></div></div>
      <div class="card"><h4 style="background:var(--red)">Premium 6 - Weeks</h4><div class="pic" role="img" aria-label="Pizza photo"></div><div class="body"><ul><li>Advantage no.1</li><li>Advantage no.2</li><li>Advantage no.3</li><li>Advantage no.4</li></ul><i class="badge" style="background:var(--red)"></i></div></div>
      <div class="card"><h4 style="background:var(--blue)">Platinum 8 - Weeks</h4><div class="pic" role="img" aria-label="Pizza photo"></div><div class="body"><ul><li>Advantage no.1</li><li>Advantage no.2</li><li>Advantage no.3</li><li>Advantage no.4</li></ul><i class="badge" style="background:var(--orange)"></i></div></div>
    </div>
    <div class="duo">
      <div><div class="head"><h3>Lena's Passion</h3><a>» view all</a></div><p>Lena was born and raised in a family kitchen, where every evening meal was a small celebration. Today she brings that same love of fresh food to busy families, cooking every dinner as if it were for her own table.</p></div>
      <div><div class="head"><h3>Testimonials</h3><a>» view all</a></div><p class="q">"Delicious!!!"<br>"Best weeknight dinner I've ever enjoyed!"<br>"Our whole family enjoyed every bite!"<br>"The food was wonderful!"<br>"The lasagna was very, very good!"</p></div>
    </div>
  </div>

  <div class="right">
    <div class="search"><h3>Search this Kitchen</h3><div class="row"><span class="field"></span><span class="btn" style="background:var(--green)">Search</span></div></div>
    <div class="box"><h3 style="background:var(--orange)">Weight Calculator</h3>
      <div class="calc">
        <div class="row">Gender: <span class="radio"></span> Male <span class="radio"></span> Female</div>
        <div class="row">Weight: <span class="field small"></span> Height: <span class="field small"></span></div>
        <div class="row">Gender: <span class="field small"></span> Age: <span class="field small"></span></div>
        <div class="row" style="justify-content:flex-end;margin:0"><span class="btn" style="background:var(--orange)">Calculate</span></div>
      </div>
    </div>
    <div class="box"><h3 style="background:var(--green)">Get in Touch</h3>
      <div class="touch">
        <label>Enter your name:</label><span class="field"></span>
        <label>Enter your email:</label><span class="field"></span>
        <label>Enter your phone number:</label><span class="field"></span>
        <label>Enter your question:</label><span class="field area"></span>
        <div class="row" style="justify-content:space-between"><span class="field" style="flex:none;width:90px;height:16px"></span><span class="btn" style="background:var(--green)">Send</span></div>
      </div>
    </div>
  </div>
</div>

<footer class="footer">
  <div class="fcols">
    <div><h4>Best Services</h4><ul><li>» How It Works</li><li>» Our Current Menu</li><li>» The Kitchen</li><li>» Catering Services</li><li>» Lena's Passion</li></ul></div>
    <div><h4>Frequently Asked Questions</h4><ul><li>» How often do you deliver?</li><li>» How soon must I cook my dinner?</li><li>» What is your delivery area?</li><li>» Can I change my weekly plan?</li><li>» How do I pause my order?</li></ul></div>
    <div><h4>Find us on:</h4><ul class="soc"><li><i style="background:var(--blue)"></i>Like us on Facepage</li><li><i style="background:var(--red)"></i>Watch us on Viewtube</li><li><i style="background:#4aa8d8"></i>Follow us on Chirper</li><li><i style="background:var(--orange)"></i>What's new</li></ul></div>
  </div>
</footer>
<div class="bottom">
  <div class="logo"><i></i>Lena's Harvest Table</div>
  <div class="copy">Lena's Harvest Table © 2011 | Privacy Policy</div>
</div>
</body>
</html>
```